Business Card Design for Fashion Tech Startup

Dear designers, we need a business card for Asia's premier fashion tech startup.!

PebbleNest is discovery e-commerce destination for busy, discerning parents in Asia featuring leading independent designers of baby, kids fashion apparel and sustainable brands from around the world.

PebbleNest is a modern, contemporary fashion tech startup targeting well-educated, well travelled and affluent parents. We're NOT your typical kiddy store!! Our design philosophy & e-commerce site is more like Vorn.com, Quenibo.com, Darwick.com, Tamsfield.com.
Updates

Hi, size of the business card should be 84mm X 55mm. Would appreciate some business card layouts in Portrait as added consideration, i fancy the idea of a Portrait business card. What's important is that the business card should pique the receiver's interest to log onto the website to learn more. Many thanks and love forward to the designs!

Target Market(s)

Though modern, classy in look, feel & positioning, PebbleNest does possess a cheeky, fun-loving personality as depicted by its logo and the segment it targets (baby, kids) though the key decision makers i.e primarily mums between 25-40 who are well educated/travelled, local & expatriates, internet/digitally savvy, mid-high income working mums.

Industry/Entity Type

E-Commerce

Requirements
Must have
• Name, designation, email, phone & mobile number.
Company url : www.pebblenest.sg
Slogan : Discovery e-commerce destination for discerning, busy parents
Nice to have
• Call to Action such as a Discount code offering 10% discount
or asking people to "Like" us on our Chatterly page/Chatterly URL

```html
<!DOCTYPE html>
<html lang="en">
<head>
<meta charset="utf-8">
<title>PebbleNest Business Card</title>
<link rel="stylesheet" href="https://fonts.googleapis.com/css2?family=Open+Sans:ital,wght@0,400;0,600;0,800;1,700&display=swap">
<style>
  :root {
    --stage: #e6e6e6;
    --salmon: #f2806d;
    --salmon-light: #f7a597;
    --navy: #36566b;
    --navy-dark: #2b4658;
    --white: #ffffff;
  }
  html, body {
    margin: 0;
    width: 1200px;
    height: 919px;
    overflow: hidden;
    background: var(--stage);
    font-family: "Open Sans", sans-serif;
  }
  .stage {
    position: relative;
    width: 1200px;
    height: 919px;
  }
  .card {
    position: absolute;
    width: 540px;
    height: 354px;
    border-radius: 22px;
    box-shadow: 0 10px 24px rgba(0,0,0,0.18);
    overflow: hidden;
  }
  /* Reverse side */
  .card-back {
    left: 40px;
    top: 190px;
    background: var(--salmon);
  }
  .slogan {
    position: absolute;
    left: 30px;
    top: 70px;
    margin: 0;
    width: 420px;
    font-style: italic;
    font-weight: 700;
    font-size: 14px;
    line-height: 1.45;
    color: var(--navy);
  }
  .pattern-area {
    position: absolute;
    right: 0;
    top: 0;
    width: 240px;
    height: 354px;
    background: radial-gradient(circle at 60% 45%, var(--salmon-light) 0%, rgba(247,165,151,0.5) 45%, rgba(242,128,109,0) 80%);
  }
  /* Front side */
  .card-front {
    left: 620px;
    top: 375px;
    background: var(--navy);
  }
  .brand-name {
    position: absolute;
    left: 28px;
    top: 26px;
    margin: 0;
    font-weight: 800;
    font-size: 46px;
    letter-spacing: 1px;
    color: var(--salmon);
  }
  .brand-dot {
    position: absolute;
    left: 70px;
    top: 118px;
    width: 120px;
    height: 120px;
    border-radius: 50%;
    border: 3px solid var(--navy-dark);
    box-sizing: border-box;
  }
  .person {
    position: absolute;
    left: 300px;
    top: 180px;
  }
  .person-name {
    margin: 0;
    font-weight: 600;
    font-size: 21px;
    letter-spacing: 1px;
    color: var(--white);
  }
  .person-title {
    margin: 0 0 14px;
    font-size: 14px;
    color: var(--salmon);
  }
  .contacts {
    list-style: none;
    margin: 0;
    padding: 0;
  }
  .contacts li {
    display: flex;
    align-items: center;
    gap: 10px;
    font-size: 15px;
    line-height: 22px;
    color: var(--white);
  }
  .contacts svg {
    width: 14px;
    height: 14px;
    flex: none;
  }
</style>
</head>
<body>
<main class="stage">
  <section class="card card-back" aria-label="Card reverse">
    <p class="slogan">Discovery e-commerce destination for discerning, busy parents<br>Like us on our Chatterly page/Chatterly URL</p>
    <div class="pattern-area" role="img" aria-label="Faint pattern of baby and kids clothing and toy illustrations"></div>
  </section>

  <section class="card card-front" aria-label="Card front">
    <h1 class="brand-name">PebbleNest</h1>
    <div class="brand-dot"></div>
    <div class="person">
      <h2 class="person-name">MARA LIND</h2>
      <p class="person-title">Managing Director</p>
      <ul class="contacts">
        <li>
          <svg viewBox="0 0 14 14" aria-hidden="true"><circle cx="7" cy="7" r="6.2" fill="none" stroke="var(--salmon)" stroke-width="1.3"/><path d="M4.6 3.8l1.3 1.4-.7 1c.5 1 1.2 1.7 2.1 2.2l1-.7 1.4 1.3-.8 1.1C6.6 9.8 4.3 7.5 3.9 4.6z" fill="var(--salmon)"/></svg>
          0400555182
        </li>
        <li>
          <svg viewBox="0 0 14 14" aria-hidden="true"><rect x="0.5" y="0.5" width="13" height="13" rx="2" fill="var(--salmon)"/></svg>
          chatterly.com/
        </li>
        <li>
          <svg viewBox="0 0 14 14" aria-hidden="true"><rect x="0.5" y="2.5" width="13" height="9" fill="var(--salmon)"/><path d="M0.5 2.5l6.5 5 6.5-5" fill="none" stroke="var(--navy)" stroke-width="1.2"/></svg>
          info@pebblenest.com
        </li>
        <li>
          <svg viewBox="0 0 14 14" aria-hidden="true"><circle cx="7" cy="7" r="6.3" fill="var(--salmon)"/><g fill="none" stroke="var(--navy)" stroke-width="0.9"><ellipse cx="7" cy="7" rx="2.8" ry="6.3"/><path d="M0.7 7h12.6M1.8 4h10.4M1.8 10h10.4"/></g></svg>
          www.pebblenest.asia
        </li>
      </ul>
    </div>
  </section>
</main>
</body>
</html>
```